Menu Design Project

Bo velle hair and beauty service menu
we need a menu to display a handful of our services to give our customers an idea of our pricing

Cutting
Ladies cuts from $35
Men's cuts from $25
All cuts are included with a wash and dry off

Quorvel colours
All over colours start from $55
price will vary depending upon length and thickness of hair

Foiling
starts from $50
Price will vary depending upon length of hair

Toners
from $30

Blowdries
from $35

Upstyling
wedding styling from $45
Please enquire for special occasion styling also

Beauty Services

Waxing
Eyebrow wax and shape $17.50
Lip $10
Chin/sides $20
Legs from $25
Bikini $20
XX $30
XXX $45
Back from $25
Chest from $25

Eyes
Eyebrow tinting $15
Eyelash tinting $20
Eyelash extensions from $90

Sandrift facials
Express facial $45
Deluxe facial $95

Acrylic nails
full set $60
Gel polish $35
Manicures from $35
Pedicures from $45

can provide logo and other images to help

Industry/Entity Type

Hair

Requirements
Must have
• must be called a service menu
must be eye catching and memorable but not excessive
Nice to have
• postcard style size hair menu on one side
beauty menu on the other side
elegant classy design
Should not have
• must not be called a price list
stay away from traditional price list style in terms of folding out leaflet

```html
<!DOCTYPE html>
<html lang="en">
<head>
<meta charset="utf-8">
<title>Bo velle Hair and Beauty – Service Menu</title>
<link rel="stylesheet" href="https://fonts.googleapis.com/css2?family=Federo&family=Andika:wght@400;700&display=swap">
<style>
  :root {
    --backdrop: #ececec;
    --card-top: #ffffff;
    --card-bottom: #e4e5e6;
    --ink: #141414;
    --pearl: rgba(232, 224, 210, 0.75);
    --gold: rgba(201, 169, 106, 0.45);
    --leaf: rgba(169, 201, 106, 0.5);
    --leaf-soft: rgba(210, 230, 170, 0.6);
    --shadow: rgba(0, 0, 0, 0.28);
  }
  * { box-sizing: border-box; margin: 0; padding: 0; }
  html, body {
    width: 1200px;
    height: 800px;
    overflow: hidden;
    background: var(--backdrop);
  }
  .canvas {
    position: relative;
    width: 1200px;
    height: 800px;
    display: flex;
    justify-content: center;
    align-items: center;
    gap: 60px;
  }
  .menu-card {
    position: relative;
    width: 430px;
    height: 620px;
    background: linear-gradient(180deg, var(--card-top) 0%, var(--card-top) 40%, var(--card-bottom) 100%);
    box-shadow: 0 10px 28px var(--shadow);
    color: var(--ink);
    text-align: center;
    overflow: hidden;
  }
  .menu-card__content {
    position: relative;
    z-index: 1;
    padding: 42px 30px 30px;
  }
  .menu-title {
    font-family: "Federo", sans-serif;
    font-weight: 400;
    font-size: 24px;
    line-height: 1.15;
    margin-bottom: 36px;
  }
  .menu-section {
    font-family: "Andika", sans-serif;
    font-size: 13px;
    line-height: 1.25;
    margin-bottom: 22px;
  }
  .menu-card--beauty .menu-section { margin-bottom: 16px; }
  .menu-section:last-child { margin-bottom: 0; }
  .menu-section__heading {
    font-weight: 700;
    font-size: 13px;
  }
  .menu-section__item { display: block; }
  .decoration {
    position: absolute;
    inset: 0;
    z-index: 0;
    pointer-events: none;
  }
  .decoration--pearls {
    background:
      radial-gradient(circle 150px at 82% 86%, var(--gold) 0%, rgba(201, 169, 106, 0) 100%),
      radial-gradient(circle 170px at 78% 62%, var(--pearl) 0%, rgba(232, 224, 210, 0) 100%);
  }
  .decoration--vines {
    background:
      radial-gradient(circle 140px at 8% 72%, var(--leaf) 0%, rgba(169, 201, 106, 0) 100%),
      radial-gradient(circle 150px at 14% 42%, var(--leaf-soft) 0%, rgba(210, 230, 170, 0) 100%);
  }
</style>
</head>
<body>
<main class="canvas">

  <section class="menu-card menu-card--hair">
    <div class="decoration decoration--pearls" role="img" aria-label="Decorative scattered pearls and golden swirling branches"></div>
    <div class="menu-card__content">
      <h1 class="menu-title">Bo velle Hair and Beauty<br>Service Menu</h1>

      <div class="menu-section">
        <h2 class="menu-section__heading">Cutting</h2>
        <span class="menu-section__item">Ladies cuts from $35</span>
        <span class="menu-section__item">Men's cuts from $25</span>
        <span class="menu-section__item">All cuts are included with a wash and dry off</span>
      </div>

      <div class="menu-section">
        <h2 class="menu-section__heading">Quorvel colours</h2>
        <span class="menu-section__item">All over colours start from $55</span>
        <span class="menu-section__item">Price will vary depending upon length and<br>thickness of hair</span>
      </div>

      <div class="menu-section">
        <h2 class="menu-section__heading">Foiling</h2>
        <span class="menu-section__item">Starts from $50</span>
        <span class="menu-section__item">Price will vary depending upon length of hair</span>
      </div>

      <div class="menu-section">
        <h2 class="menu-section__heading">Toners</h2>
        <span class="menu-section__item">From $30</span>
      </div>

      <div class="menu-section">
        <h2 class="menu-section__heading">Blowdries</h2>
        <span class="menu-section__item">From $35</span>
        <span class="menu-section__item">Price will vary depending upon length and<br>thickness of hair</span>
      </div>

      <div class="menu-section">
        <h2 class="menu-section__heading">Upstyling</h2>
        <span class="menu-section__item">Wedding styling from $45</span>
        <span class="menu-section__item">Please also enquire for special occasion styling</span>
      </div>
    </div>
  </section>

  <section class="menu-card menu-card--beauty">
    <div class="decoration decoration--vines" role="img" aria-label="Decorative green bubbles, butterfly and curling vines"></div>
    <div class="menu-card__content">
      <h1 class="menu-title">Bo velle Hair and Beauty<br>Service Menu</h1>

      <div class="menu-section">
        <h2 class="menu-section__heading">Waxing</h2>
        <span class="menu-section__item">Eyebrow wax and shape $17.50</span>
        <span class="menu-section__item">Lip $10</span>
        <span class="menu-section__item">Chin/sides $20</span>
        <span class="menu-section__item">Legs from $25</span>
        <span class="menu-section__item">Bikini $20</span>
        <span class="menu-section__item">XX $30</span>
        <span class="menu-section__item">XXX $45</span>
        <span class="menu-section__item">Back from $25</span>
        <span class="menu-section__item">Chest from $25</span>
      </div>

      <div class="menu-section">
        <h2 class="menu-section__heading">Eyes</h2>
        <span class="menu-section__item">Eyebrow tinting $15</span>
        <span class="menu-section__item">Eyelash tinting $20</span>
        <span class="menu-section__item">Eyelash extensions from $90</span>
      </div>

      <div class="menu-section">
        <h2 class="menu-section__heading">Sandrift facials</h2>
        <span class="menu-section__item">Express facial $45</span>
        <span class="menu-section__item">Deluxe facial $95</span>
      </div>

      <div class="menu-section">
        <h2 class="menu-section__heading">Acrylic nails</h2>
        <span class="menu-section__item">Full set $60</span>
        <span class="menu-section__item">Gel polish $35</span>
        <span class="menu-section__item">Manicures from $35</span>
        <span class="menu-section__item">Pedicures from $45</span>
      </div>
    </div>
  </section>

</main>
</body>
</html>
```